Veltrano - Mechanic/Collision Center Business Card

We're looking for a business card design for our mechanic/ collision repair shop.

Can be with colours or monochromatic.

See the attached files.

Many thanks

```html
<!DOCTYPE html>
<html lang="en">
<head>
<meta charset="utf-8">
<title>Veltrano – Business Card</title>
<link href="https://fonts.googleapis.com/css2?family=Roboto:wght@400;500;700;900&display=swap" rel="stylesheet">
<style>
  :root {
    --backdrop: #a7a7a7;
    --card: #ffffff;
    --ink: #1f2326;
    --text-grey: #4a4d50;
    --brand-blue: #1e9fdc;
    --car-grey: #7c7d80;
    --car-blue: #22a2dc;
  }
  * { margin: 0; padding: 0; box-sizing: border-box; }
  html, body {
    width: 1200px; height: 954px; overflow: hidden;
    background: var(--backdrop);
    font-family: "Roboto", Arial, sans-serif;
  }
  .canvas { position: relative; width: 1200px; height: 954px; }
  .card {
    position: absolute; top: 344px;
    width: 525px; height: 300px;
    background: var(--card); overflow: hidden;
  }
  .card--front { left: 68px; }
  .card--back { left: 606px; }

  .brand-name {
    position: absolute; left: 28px; top: 30px;
    font-weight: 900; font-size: 36px; letter-spacing: 1px;
    color: var(--ink); text-transform: uppercase; line-height: 1;
  }
  .person-name {
    position: absolute; left: 28px; top: 103px;
    font-weight: 700; font-size: 20px; color: var(--brand-blue);
  }
  .person-role {
    position: absolute; left: 28px; top: 128px;
    font-size: 15px; color: var(--text-grey);
  }
  .address {
    position: absolute; left: 28px; top: 164px;
    font-size: 15px; line-height: 19px; color: var(--text-grey);
  }
  .contact-list {
    position: absolute; left: 28px; top: 219px;
    list-style: none; font-size: 15px; line-height: 19px; color: var(--text-grey);
  }
  .contact-list li { display: flex; align-items: center; gap: 6px; }
  .contact-list svg { width: 13px; height: 13px; fill: var(--brand-blue); flex: none; }

  .vehicle-art--front {
    position: absolute; left: 245px; top: 62px; width: 280px; height: 238px;
    background: linear-gradient(100deg, var(--car-grey) 0%, var(--car-grey) 42%, var(--car-blue) 48%, var(--car-blue) 100%);
    border-radius: 60px 40px 0 0;
  }
  .vehicle-art--back {
    position: absolute; left: 143px; top: 70px; width: 235px; height: 92px;
    background: linear-gradient(90deg, var(--car-grey) 0%, var(--car-grey) 22%, var(--car-blue) 28%, var(--car-blue) 72%, var(--car-grey) 78%, var(--car-grey) 100%);
    border-radius: 30px 30px 10px 10px;
  }
  .brand-name--centered {
    left: 0; right: 0; top: 172px; text-align: center;
    font-size: 44px;
  }
</style>
</head>
<body>
<main class="canvas">
  <section class="card card--front" aria-label="Business card front">
    <div class="brand-name">Veltrano</div>
    <div class="person-name">Marcus Hale</div>
    <div class="person-role">Manager</div>
    <p class="address">Your address, city<br>state, ZIP 0000</p>
    <ul class="contact-list">
      <li><svg viewBox="0 0 24 24" aria-hidden="true"><path d="M6.6 10.8a15 15 0 0 0 6.6 6.6l2.2-2.2c.3-.3.7-.4 1-.2 1.1.4 2.3.6 3.6.6.6 0 1 .4 1 1V20c0 .6-.4 1-1 1A17 17 0 0 1 3 4c0-.6.4-1 1-1h3.5c.6 0 1 .4 1 1 0 1.3.2 2.5.6 3.6.1.3 0 .7-.2 1z"/></svg>123-456-2100</li>
      <li><svg viewBox="0 0 24 24" aria-hidden="true"><path d="M2 5h20v14H2z M2 5l10 8 10-8" fill="var(--brand-blue)" stroke="#fff" stroke-width="1.5"/></svg>youremail@veltranomail.com</li>
      <li><svg viewBox="0 0 24 24" aria-hidden="true"><circle cx="12" cy="12" r="10"/><path d="M2 12h20M12 2c3 3 3 17 0 20M12 2c-3 3-3 17 0 20" stroke="#fff" stroke-width="1.4" fill="none"/></svg>www.yourwebsite.com</li>
    </ul>
    <div class="vehicle-art--front" role="img" aria-label="Illustration of a grey and a blue sports car front with a wrench"></div>
  </section>

  <section class="card card--back" aria-label="Business card back">
    <div class="vehicle-art--back" role="img" aria-label="Illustration of three car fronts, grey, blue and grey, with a wrench"></div>
    <div class="brand-name brand-name--centered">Veltrano</div>
  </section>
</main>
</body>
</html>
```